1 x Double Page Spread for Book Design Project.

Student Wellbeing Planner Book, to be used by teenagers aged 12-18. Needs to be colourful, fun and engaging.

Require a double page spread, left and right hand page to be designed in 4 colour.

The final design should communicate positive learning in an easy to understand format.

Target Market(s)

Teenagers Aged 12-18 years old

Industry/Entity Type

Learning

Requirements
Must have
• Must have a more colourful and updated look than attached current layout.

Must have the weekly planner functionality as per the attached layout.

```html
<!DOCTYPE html>
<html lang="en">
<head>
<meta charset="utf-8">
<title>Student Planner – Weekly Spread</title>
<link rel="stylesheet" href="https://fonts.googleapis.com/css2?family=Fredoka:wght@500;600&family=Fira+Sans+Condensed:ital,wght@0,400;0,600;1,400;1,600;1,700&family=Raleway:wght@300;400&display=swap">
<style>
:root{
  --orange:#f0582a;
  --navy:#1d5aa6;
  --blue:#3fb6ea;
  --pale-blue:#a7d6f2;
  --green-row:#dff0d8;
  --green-box:#d5ebd0;
  --rule:#9aa3a8;
  --yellow:#fbb92c;
  --label-yellow:#fdd86a;
  --pink:#f7d3dc;
  --red:#e84a2a;
  --text:#3a3a3a;
  --grey:#7b8186;
}
*{box-sizing:border-box;margin:0;padding:0}
html,body{width:1200px;height:781px;overflow:hidden;background:#fff}
body{position:relative;font-family:"Fira Sans Condensed",sans-serif;color:var(--text)}
.abs{position:absolute}

/* page strips */
.strip-left{left:263px;top:0;width:20px;height:781px;background:var(--pale-blue)}
.strip-right{left:1086px;top:0;width:114px;height:781px;background:var(--pale-blue)}

/* section label */
.section-label{left:0;top:0;width:292px;height:80px;background:var(--label-yellow);
  font-family:"Fredoka",sans-serif;font-weight:600;color:var(--orange);font-size:31px;line-height:27px;padding:17px 0 0 27px;letter-spacing:-.3px}
.section-label::before,.section-label::after{content:"";position:absolute;top:-4px;width:46px;height:18px;background:#efe4c4;opacity:.85}
.section-label::before{left:48px;transform:rotate(-8deg)}
.section-label::after{right:10px;transform:rotate(10deg)}

/* left sidebar */
.topic-dot{left:4px;top:96px;width:34px;height:34px;border-radius:50%;background:#fbe21a;border:3px solid var(--navy)}
.topic-title{left:48px;top:98px;font-family:"Fira Sans Condensed",sans-serif;font-style:italic;font-weight:700;font-size:25px;line-height:25px;color:var(--navy)}
.tips{left:34px;top:154px;width:210px;font-size:8px;line-height:10.4px}
.tips h3{font-style:italic;font-weight:700;color:var(--red);font-size:11.5px;line-height:14px}
.tips h4{font-style:italic;font-weight:700;font-size:9px;line-height:11px}
.tips .green{color:#6cb33f}
.tips .darkgreen{color:#2c7a3b}
.tips .red{color:var(--red)}
.tips ul{list-style:none}
.tips li{padding-left:9px;text-indent:-9px}
.tips li::before{content:"* "}
.tips.lower{top:325px}
.tips.lower li{font-size:8px}
.callout{left:0;top:270px;width:256px;height:44px}
.callout p{position:absolute;left:42px;top:11px;font-style:italic;font-weight:600;font-size:10px;line-height:13px;color:#555}
.closing{left:34px;top:650px;font-style:italic;font-weight:600;color:var(--red);font-size:12px}
.quote{left:0;top:678px;width:258px;height:62px}
.quote p{position:absolute;left:24px;top:11px;font-family:"Raleway",sans-serif;font-style:italic;font-size:12px;line-height:13px;color:#555}
.quote span{display:block;font-style:normal;margin-top:5px}
.page-no{font-family:"Fira Sans Condensed",sans-serif;font-weight:600;font-size:12px;top:758px}

/* headings */
.month{left:312px;top:26px;font-family:"Fredoka",sans-serif;font-weight:600;font-size:31px;color:var(--orange);letter-spacing:-.5px}
.year{left:636px;top:24px;font-family:"Fredoka",sans-serif;font-weight:600;font-size:32px;color:var(--navy)}
.mini-cal{left:783px;top:26px;width:394px;font-size:6px;color:#333}
.mini-cal .cal-title{text-align:center;font-family:"Raleway",sans-serif;font-size:11px;margin-left:-10px;padding-bottom:1px;border-bottom:1px solid #333}
.mini-cal .row{display:grid;grid-template-columns:repeat(30,1fr);text-align:center;margin-top:3px}
.mini-cal .days{font-style:italic;font-weight:700}

/* planner columns */
.col-head{top:77px;height:17px;background:var(--blue);color:#fff;font-weight:600;font-size:11px;line-height:17px;padding-left:5px}
.priorities{left:306px;width:259px}
.todo{left:636px;width:445px;display:flex;gap:0}
.todo .value{margin-left:80px}
.todo .value b{color:#fde24a;font-weight:600}
.todo .week{margin-left:39px}
.todo .week-box{display:inline-block;width:36px;height:12px;background:#fff;vertical-align:middle;margin-left:4px}
.todo .done{margin-left:auto;margin-right:6px;font-size:8px}
.todo .done i{display:inline-block;width:10px;height:10px;border:1px solid #fff;vertical-align:middle;margin-left:2px;position:relative}
.todo .done i::after{content:"";position:absolute;left:2px;top:0;width:3px;height:6px;border:solid #fff;border-width:0 1.5px 1.5px 0;transform:rotate(40deg)}

.day{position:absolute;
  background:repeating-linear-gradient(to bottom,transparent 0 11.7px,var(--rule) 11.7px 12.7px);
  background-position:0 14px;background-repeat:repeat-y}
.day .head{height:14px;background:var(--green-row);font-size:9.5px;line-height:14px;padding-left:4px;color:#333}
.day .head b{font-weight:600}
.day.faded .head{color:#9fb4a3}
.day .checks{position:absolute;right:2px;top:16px;bottom:0;width:10px;
  background:repeating-linear-gradient(to bottom,var(--green-box) 0 10px,transparent 10px 12.7px)}
.weekend{position:absolute;background:var(--green-row);font-size:9.5px;padding:4px 0 0 4px;color:#333}
.weekend b{font-weight:600}

/* vocabulary */
.vocab{left:1090px;top:83px;width:110px;height:182px;background:#dedfe0}
.vocab h3{background:#5c6064;color:#fff;font-style:italic;font-weight:700;font-size:14px;line-height:13px;text-align:center;padding:6px 0 5px 8px;border-radius:12px 0 0 12px}
.vocab ul{list-style:none;text-align:center;font-family:"Raleway",sans-serif;font-size:10.5px;line-height:14.2px;color:#444;padding-top:9px}

/* rate your week */
.rate{left:1100px;top:296px;width:100px;height:204px;background:var(--yellow)}
.rate-tick{left:1090px;top:278px;width:26px;height:26px;border-radius:50%;background:#fff;border:2px solid var(--yellow)}
.rate h3{position:absolute;left:16px;top:2px;color:#fff;font-style:italic;font-weight:700;font-size:19px;line-height:18px;text-align:center}
.rate h3 small{font-size:17px;display:block}
.rate .scale{position:absolute;left:24px;top:66px;list-style:none;font-style:italic;font-weight:700;font-size:9.5px;line-height:13.4px;color:#333;border-left:2px solid var(--red);padding-left:4px;margin-left:-11px}
.rate .scale span{font-family:"Raleway",sans-serif;font-style:normal;font-weight:400;color:#777;margin-left:4px}

.photo{left:1085px;top:515px;width:115px;height:266px;border-radius:60px 0 0 0;
  background:linear-gradient(160deg,#f5e3c8 0%,#e9c89a 45%,#8a4aa8 80%,#6e2f92 100%)}
</style>
</head>
<body>
<div class="abs strip-left"></div>
<div class="abs strip-right"></div>

<!-- left page -->
<div class="abs section-label">CAREER &amp; TIME<br>MANAGEMENT</div>
<div class="abs topic-dot"></div>
<h2 class="abs topic-title">Procrastination/<br>Desicion making</h2>

<div class="abs tips">
  <h3>How easy is to delay doing things?</h3>
  <h4 class="green">Why do you do it?</h4>
  <h4 class="darkgreen">Procrastination can stem from:</h4>
  <ul>
    <li>avoiding task you are not familiar with.</li>
    <li>being afraid of unpleasant outcomes.</li>
    <li>a desire to achive the perfect result.</li>
    <li>a lack of self confidence to begin.</li>
    <li>an obsession with detail.</li>
    <li>not coping with study demands.</li>
    <li>a lack of prioritising and time management.</li>
  </ul>
</div>

<div class="abs callout">
  <svg width="256" height="44" viewBox="0 0 256 44"><path d="M0 0H236L256 22L236 44H0L14 22Z" fill="#f4a9a0"/><path d="M14 0H236L256 22L236 44H14Z" fill="var(--pink)"/></svg>
  <p>Overcoming the problem requires disciplined<br>desicion making.</p>
</div>

<div class="abs tips lower">
  <h4 class="red">The following strategies are effective in combating<br>procrastination</h4>
  <ul>
    <li>identify tasks that you regularly delay.</li>
    <li>Berum et aut offici voluptas ulparit labores volupta tquatib usantem perferiam.</li>
    <li>Illa cor seque adi cus demperupta nis assu.</li>
    <li>Berum et aut offici voluptas ulparit labores volupta tquatib usantem perferiam.</li>
    <li>Illa cor seque adi cus demperupta nis assu.</li>
  </ul>
  <h4 class="red">Positive self talk is beneficial.</h4>
  <ul>
    <li>Berum et aut offici voluptas ulparit labores volupta tquatib usantem perferiam.</li>
    <li>Illa cor seque adi cus demperupta nis assu.</li>
    <li>Berum et aut offici voluptas ulparit labores volupta tquatib usantem perferiam.</li>
    <li>Illa cor seque adi cus demperupta nis assu.</li>
  </ul>
  <h4 class="red">Beware of the "bouncing effect"</h4>
  <ul>
    <li>Berum et aut offici voluptas ulparit labores volupta tquatib usantem perferiam.</li>
    <li>Illa cor seque adi cus demperupta nis assu.</li>
    <li>Berum et aut offici voluptas ulparit labores volupta tquatib usantem perferiam.</li>
  </ul>
  <h4 class="red">Commiting yourself immediately to one task</h4>
  <ul>
    <li>Berum et aut offici voluptas ulparit labores volupta tquatib usantem perferiam.</li>
    <li>Illa cor seque adi cus demperupta nis assu.</li>
    <li>Berum et aut offici voluptas ulparit labores volupta tquatib usantem perferiam.</li>
  </ul>
  <h4 class="red">Once you have completed a trask, especially ahead of time, reward yourself.</h4>
</div>
<p class="abs closing">Being effective means being in control NOW.</p>

<div class="abs quote">
  <svg width="258" height="62" viewBox="0 0 258 62"><path d="M0 4L40 1L90 5L140 2L190 5L232 2L246 10L241 20L250 30L243 40L252 50L246 60L180 58L120 61L60 58L0 60Z" fill="#e4e5e6"/></svg>
  <p>"Procrastination is the art of keeping<br>up with yesterday."<span>- Anonymous.</span></p>
</div>
<p class="abs page-no" style="left:6px">96</p>

<!-- right side headings -->
<h1 class="abs month">August/September</h1>
<p class="abs year">2012</p>
<div class="abs mini-cal">
  <div class="cal-title">September</div>
  <div class="row days"><span>S</span><span>S</span><span>M</span><span>T</span><span>W</span><span>T</span><span>F</span><span>S</span><span>S</span><span>M</span><span>T</span><span>W</span><span>T</span><span>F</span><span>S</span><span>S</span><span>M</span><span>T</span><span>W</span><span>T</span><span>F</span><span>S</span><span>S</span><span>M</span><span>T</span><span>W</span><span>T</span><span>F</span><span>S</span><span>S</span></div>
  <div class="row"><span>1</span><span>2</span><span>3</span><span>4</span><span>5</span><span>6</span><span>7</span><span>8</span><span>9</span><span>10</span><span>11</span><span>12</span><span>13</span><span>14</span><span>15</span><span>16</span><span>17</span><span>18</span><span>19</span><span>20</span><span>21</span><span>22</span><span>23</span><span>24</span><span>25</span><span>26</span><span>27</span><span>28</span><span>29</span><span>30</span></div>
</div>

<!-- priorities column -->
<div class="abs col-head priorities">Priorities / Due dates</div>
<div class="day" style="left:306px;top:95px;width:259px;height:114px"><div class="head">Monday <b>27</b></div><div class="checks"></div></div>
<div class="day" style="left:306px;top:211px;width:259px;height:116px"><div class="head">Tuesday <b>28</b></div><div class="checks"></div></div>
<div class="day" style="left:306px;top:329px;width:259px;height:114px"><div class="head">Wednesday <b>29</b></div><div class="checks"></div></div>
<div class="day" style="left:306px;top:445px;width:259px;height:116px"><div class="head">Thursday <b>30</b></div><div class="checks"></div></div>
<div class="day" style="left:306px;top:563px;width:259px;height:116px"><div class="head">Friday <b>31</b></div><div class="checks"></div></div>
<div class="weekend" style="left:306px;top:687px;width:259px;height:33px">Saturday <b>1</b></div>
<div class="weekend" style="left:306px;top:722px;width:259px;height:34px">Sunday &nbsp;<b>2</b></div>

<!-- things to do column -->
<div class="abs col-head todo"><span>Things to do</span><span class="value">Value for life: <b>ENTHUSIAM!</b></span><span class="week">Week:<span class="week-box"></span></span><span class="done">Done<i></i></span></div>
<div class="day faded" style="left:636px;top:95px;width:445px;height:114px"><div class="head">Monday <b>27</b></div><div class="checks"></div></div>
<div class="day faded" style="left:636px;top:211px;width:445px;height:116px"><div class="head">Tuesday <b>28</b></div><div class="checks"></div></div>
<div class="day faded" style="left:636px;top:329px;width:445px;height:114px"><div class="head">Wednesday <b>29</b></div><div class="checks"></div></div>
<div class="day faded" style="left:636px;top:445px;width:445px;height:116px"><div class="head">Thursday <b>30</b></div><div class="checks"></div></div>
<div class="day faded" style="left:636px;top:563px;width:445px;height:116px"><div class="head">&nbsp;</div><div class="checks"></div></div>
<div class="weekend" style="left:636px;top:687px;width:445px;height:33px;background:linear-gradient(var(--green-row) 0 16px,#fff 16px 17px,var(--green-row) 17px)"></div>
<div class="weekend" style="left:636px;top:722px;width:445px;height:34px;background:linear-gradient(var(--green-row) 0 16px,#fff 16px 17px,var(--green-row) 17px)"></div>

<!-- vocabulary -->
<div class="abs vocab">
  <h3>Vocabulary<br>builder</h3>
  <ul><li>matted</li><li>guaranteed</li><li>imaginative</li><li>draught</li><li>jettison</li><li>barely</li><li>hilarious</li><li>pincer</li><li>category</li></ul>
</div>

<!-- rate your week -->
<div class="abs rate">
  <h3>RATE<small>your</small>WEEK</h3>
  <ul class="scale">
    <li>10<span>Great!</span></li><li>9</li><li>8</li><li>7</li><li>6</li><li>5</li><li>4</li><li>3</li><li>2</li><li>1<span>Fair.</span></li>
  </ul>
</div>
<div class="abs rate-tick">
  <svg width="22" height="22" viewBox="0 0 22 22"><rect x="4" y="5" width="12" height="12" fill="none" stroke="var(--red)" stroke-width="1.5"/><path d="M6 11L10 15L19 3" fill="none" stroke="var(--red)" stroke-width="2.5" stroke-linecap="round"/></svg>
</div>

<div class="abs photo" role="img" aria-label="Photo of a cheerful teenage girl pulling a funny face"></div>
<p class="abs page-no" style="left:1183px;color:#fff">97</p>
</body>
</html>
```